Mobile phone signal boosting solutions needs a website

We need a website design for the reselling of a mobile signal boosting product set. These solutions are Travik exempt and will provide an indoor signal for mobile phones. We would like to see designs that incorporate the colours and feel of our logo. The domain will be
nestorbolt.com / co.uk
Overview of the company and how it is to be used: Nestor Bolt (domain name) will work with business and end user to provide mobile signal boosting – where people struggle indoors with a mobile signal our solutions will help by finding the smallest signal and boosting it, allowing users to use voice and data over their mobile network (please note this is not wireless signal boosting)
Number of Pages:
-Home
-Solutions / How it works
-Case Studies
-Contact
Text content: Currently just use placeholders
Technical specs : Wordpress and ability to use CMS if that’s relevant
Target Market(s)
Business professional all markets /high end residential
Coding
Coded - Design and coding required
Number of Pages Required
4 page
Look and feel

```html
<!DOCTYPE html>
<html lang="en">
<head>
<meta charset="utf-8">
<title>Nestor Bolt – Mobile Signal Booster</title>
<link href="https://fonts.googleapis.com/css2?family=Roboto:wght@400;500;700;900&family=Roboto+Condensed:wght@400;500&display=swap" rel="stylesheet">
<style>
:root{
  --yellow:#fcc016;
  --amber:#f9a71f;
  --ink:#111111;
  --text:#666666;
  --dark:#26282c;
  --white:#ffffff;
}
*{margin:0;padding:0;box-sizing:border-box}
html,body{width:1200px;height:3604px;overflow:hidden}
body{position:relative;font-family:'Roboto',sans-serif;color:var(--ink);background:var(--white)}
.abs{position:absolute}
.btn{position:absolute;display:flex;align-items:center;justify-content:center;font-weight:500;font-size:15px;color:var(--ink);text-decoration:none}
.btn-yellow{background:var(--yellow)}
.btn-white{background:var(--white)}

/* header */
.topline{left:0;top:0;width:1200px;height:4px;background:var(--amber)}
.header-cta{left:933px;top:24px;width:154px;height:42px}
.nav{top:83px;right:113px;display:flex;gap:34px;font-size:15px;color:#222}
.logo-tab{left:112px;top:100px;width:224px;height:82px;z-index:2}
.logo{left:112px;top:112px;width:224px;text-align:center;z-index:3}
.logo-name{font-family:'Roboto Condensed',sans-serif;font-size:30px;font-weight:500;color:var(--ink);letter-spacing:-0.5px}
.logo-sub{font-size:10px;font-weight:700;color:var(--amber);letter-spacing:.3px}

/* hero */
.hero{left:0;top:122px;width:1200px;height:506px;background:linear-gradient(100deg,#fbb51e 0%,#fcc216 45%,#f9b928 100%)}
.hero-title{left:108px;top:266px;font-size:64px;line-height:66px;font-weight:900;color:var(--ink);letter-spacing:.5px}
.hero-text{left:112px;top:404px;width:420px;font-size:15.5px;line-height:27px;color:#1c1c1c}
.hero-cta{left:112px;top:503px;width:127px;height:42px}
.hero-visual{left:630px;top:133px;width:530px;height:495px;background:linear-gradient(180deg,rgba(255,255,255,.25),rgba(120,80,20,.35))}

/* about & solutions */
.frame{border:4px solid var(--yellow)}
.photo{border-radius:4px}
.section-title{font-size:42px;font-weight:700;color:var(--ink)}
.body-text{font-size:13.6px;line-height:27.4px;color:var(--text)}
.list{list-style:none}
.list li{display:flex;align-items:center;gap:17px;height:34px;font-size:13.6px;color:var(--text)}

/* case studies */
.cases{left:0;top:1911px;width:1200px;height:780px}
.cases-title{left:0;top:1978px;width:1200px;text-align:center;font-size:42px;font-weight:700;color:var(--white)}
.card{top:2062px;width:309px;height:408px;background:var(--white);text-align:center}
.card-img{position:absolute;left:10px;top:11px;width:289px;height:201px}
.card-title{position:absolute;left:10px;top:232px;width:289px;font-size:16px;line-height:25px;font-weight:500;color:#222}
.card-text{position:absolute;left:30px;top:296px;width:249px;font-size:12.4px;line-height:20px;color:var(--text)}
.card-link{position:absolute;left:0;top:364px;width:309px;font-size:15px;font-weight:700;color:var(--amber);text-decoration:underline}
.cases-cta{left:537px;top:2508px;width:127px;height:42px}

/* contact */
.contact-title{left:0;top:2720px;width:1200px;text-align:center;font-size:42px;font-weight:700}
.field{left:112px;width:471px;height:64px;background:var(--white);border-radius:8px;box-shadow:0 3px 14px rgba(0,0,0,.12);font-size:13.5px;color:#777;padding:22px 0 0 42px}
.message{left:617px;top:2807px;width:471px;height:330px;background:var(--white);border-radius:8px;box-shadow:0 3px 14px rgba(0,0,0,.12);font-size:13.5px;color:#777;padding:26px 0 0 42px}
.submit{left:112px;top:3073px;width:471px;height:64px;border-radius:8px;background:linear-gradient(180deg,#fcc016,#f9ae22);font-size:13.5px;font-weight:700}

/* footer */
.footer{left:0;top:3237px;width:1200px;height:367px;background:var(--dark)}
.footer-logo{left:0;top:3395px;width:1200px;text-align:center;color:var(--white)}
.footer-logo .logo-name{color:var(--white);font-size:44px}
.footer-logo .logo-sub{color:var(--white);font-family:'Roboto Condensed',sans-serif;font-size:19px;font-weight:500;margin-top:2px}
.footer-nav{left:0;top:3513px;width:1200px;display:flex;justify-content:center;gap:46px;font-size:15.5px;color:var(--white)}
.copyright{left:0;top:3556px;width:1200px;text-align:center;font-size:15.5px;color:var(--white)}
</style>
</head>
<body>

<!-- header -->
<div class="abs topline"></div>
<a class="btn btn-yellow header-cta" href="#">Get Started</a>
<nav class="abs nav"><span>Home</span><span>Solutions/How It Works</span><span>Case Studies</span><span>Contact Us</span></nav>

<!-- hero -->
<section class="abs hero"></section>
<div class="abs hero-visual" role="img" aria-label="Smiling couple looking at a phone, framed by rising signal bars"></div>
<svg class="abs logo-tab" viewBox="0 0 224 82"><path d="M0 22 L224 22 L200 82 L24 82 Z" fill="#fff"/></svg>
<div class="abs logo">
  <div class="logo-name">Nestor Bolt</div>
  <div class="logo-sub">MOBILE SIGNAL BOOSTER</div>
</div>
<h1 class="abs hero-title">MOBILE SIGNAL<br>BOOSTER</h1>
<p class="abs hero-text">Lorem Ipsum is simply dummy text of the printing and typesetting industry. Lorem Ipsum has been the industry's standard dummy text ever since</p>
<a class="btn btn-white hero-cta" href="#">Get Started</a>

<!-- about -->
<div class="abs frame" style="left:95px;top:726px;width:272px;height:293px"></div>
<div class="abs photo" style="left:131px;top:762px;width:430px;height:465px;background:linear-gradient(135deg,#1f6ea8 0%,#d9b34a 55%,#c9a338 100%)" role="img" aria-label="Smiling man on a yellow sofa using his phone"></div>
<h2 class="abs section-title" style="left:615px;top:786px">ABOUT US</h2>
<p class="abs body-text" style="left:615px;top:851px;width:470px">Lorem Ipsum is simply dummy text of the printing and typesetting industry. Lorem Ipsum has been the industry's standard dummy text ever since the 1500s, when an unknown printer took a galley of type and scrambled it to make a type specimen book. It has survived not only five centuries, but also the leap into electronic typesetting, remaining essentially unchanged. It was popularised in the 1960s with the release</p>
<p class="abs body-text" style="left:615px;top:1043px;width:470px">Lorem Ipsum is simply dummy text of the printing and typesetting industry. Lorem Ipsum has been the industry's standard dummy text ever since the 1500s, when an unknown printer took a galley</p>
<a class="btn btn-yellow" style="left:615px;top:1148px;width:131px;height:42px" href="#">Read More</a>

<!-- solutions -->
<div class="abs frame" style="left:836px;top:1291px;width:273px;height:295px"></div>
<div class="abs photo" style="left:641px;top:1327px;width:430px;height:465px;background:linear-gradient(135deg,#8a7a5a 0%,#c9c2ad 45%,#9aa877 100%)" role="img" aria-label="Woman showing a phone to an older man holding a cup"></div>
<h2 class="abs section-title" style="left:130px;top:1357px">OUR SOLUTIONS</h2>
<p class="abs body-text" style="left:130px;top:1419px;width:470px">Lorem Ipsum is simply dummy text of the printing and typesetting industry. Lorem Ipsum has been the industry's standard dummy text ever since the 1500s, when an unknown printer took a galley of type and scrambled it to make a type specimen book.</p>
<ul class="abs list" style="left:130px;top:1544px">
  <li><svg width="36" height="14" viewBox="0 0 36 14"><path d="M0 7H34M27 1L34 7L27 13" fill="none" stroke="#444" stroke-width="2"/></svg>Lorem Ipsum is simply dummy text of the printing</li>
  <li><svg width="36" height="14" viewBox="0 0 36 14"><path d="M0 7H34M27 1L34 7L27 13" fill="none" stroke="#444" stroke-width="2"/></svg>Lorem Ipsum is simply</li>
  <li><svg width="36" height="14" viewBox="0 0 36 14"><path d="M0 7H34M27 1L34 7L27 13" fill="none" stroke="#444" stroke-width="2"/></svg>Lorem Ipsum is simply dummy text</li>
  <li><svg width="36" height="14" viewBox="0 0 36 14"><path d="M0 7H34M27 1L34 7L27 13" fill="none" stroke="#444" stroke-width="2"/></svg>Lorem Ipsum of the printing</li>
</ul>
<a class="btn btn-yellow" style="left:130px;top:1709px;width:131px;height:42px" href="#">Read More</a>

<!-- case studies -->
<svg class="abs cases" viewBox="0 0 1200 780" preserveAspectRatio="none">
  <defs><linearGradient id="caseGrad" x1="0" y1="0" x2="0" y2="1"><stop offset="0" stop-color="#f9a225"/><stop offset="1" stop-color="#fcc316"/></linearGradient></defs>
  <path d="M0 0H1200V763C1080 770 900 745 700 712C520 684 380 700 300 702C180 706 80 725 0 758Z" fill="url(#caseGrad)"/>
</svg>
<h2 class="abs cases-title">CASE STUDIES</h2>

<article class="abs card" style="left:112px">
  <div class="card-img" style="background:linear-gradient(135deg,#b8a89a,#8a6a4f)" role="img" aria-label="Hands holding a phone above a laptop"></div>
  <h3 class="card-title">LOREM IPSUM IS SIMPLY DUMMY TEXT OF THE PRNTING</h3>
  <p class="card-text">Lorem Ipsum is simply dummy text of the printing and typesetting industry. Lorem Ipsum has been the industry's</p>
  <a class="card-link" href="#">View More</a>
</article>
<article class="abs card" style="left:446px">
  <div class="card-img" style="background:linear-gradient(135deg,#5b4a3a,#d7c39a)" role="img" aria-label="Two women sharing a phone at a table"></div>
  <h3 class="card-title">LOREM IPSUM IS SIMPLY DUMMY TEXT OF THE PRNTING</h3>
  <p class="card-text">Lorem Ipsum is simply dummy text of the printing and typesetting industry. Lorem Ipsum has been the industry's</p>
  <a class="card-link" href="#">View More</a>
</article>
<article class="abs card" style="left:780px">
  <div class="card-img" style="background:linear-gradient(135deg,#9a8a78,#d8a24a)" role="img" aria-label="Woman on a sofa smiling at her phone"></div>
  <h3 class="card-title">LOREM IPSUM IS SIMPLY DUMMY TEXT OF THE PRNTING</h3>
  <p class="card-text">Lorem Ipsum is simply dummy text of the printing and typesetting industry. Lorem Ipsum has been the industry's</p>
  <a class="card-link" href="#">View More</a>
</article>
<a class="btn btn-white cases-cta" href="#">Get Started</a>

<!-- contact -->
<h2 class="abs contact-title">GET IN TOUCH WITH US</h2>
<div class="abs field" style="top:2807px">Full Name</div>
<div class="abs field" style="top:2895px">Contact Number</div>
<div class="abs field" style="top:2985px">Email Address</div>
<a class="btn submit" href="#">Submit Here</a>
<div class="abs message">Your Message Goes Here...</div>

<!-- footer -->
<footer class="abs footer"></footer>
<div class="abs footer-logo">
  <div class="logo-name">Nestor Bolt</div>
  <div class="logo-sub">MOBILE SIGNAL BOOSTER</div>
</div>
<nav class="abs footer-nav"><span>Home</span><span>|</span><span>Solutions/How It Works</span><span>|</span><span>Case Studies</span><span>|</span><span>Contact Us</span></nav>
<p class="abs copyright">© Copyright 2023 Nestor Bolt | All Rights Reserved.</p>

</body>
</html>
```